Generative AI radar Infographics

I want to create an infographic called "Machine Learning Prospect Compass for Tender Replies". (see slide 3 of the PowerPoint file). I want to use it on social media (ConnectHub and Website). I added 2 inspiration graphics in my brief (see slide 2 of the PowerPoint). I want to add my logo on the infographic. (I also uploaded my company logos). You can find model detailed instructions on slide 1 of the PowerPoint.
Business development and sales
I am a business consultant. I will be using this infographics on Connecthub and in my powerpoint presentations to clients

```html
<!DOCTYPE html>
<html lang="en">
<head>
<meta charset="utf-8">
<title>Machine Learning Prospect Compass for Tender Replies</title>
<link href="https://fonts.googleapis.com/css2?family=Montserrat:wght@600;700&family=Lato:wght@700&display=swap" rel="stylesheet">
<style>
  :root {
    --teal: #0b93b8;
    --navy: #0b2c3f;
    --ice: #c3effd;
    --white: #ffffff;
  }
  html, body {
    margin: 0;
    padding: 0;
    overflow: hidden;
    background: var(--white);
  }
  .canvas {
    position: relative;
    width: 1200px;
    height: 1200px;
    overflow: hidden;
    background: var(--white);
    font-family: "Montserrat", sans-serif;
  }
  .header {
    position: absolute;
    left: 0; top: 0;
    width: 1200px;
    height: 223px;
    background: var(--teal);
    display: flex;
    align-items: center;
    justify-content: center;
  }
  .title {
    margin: 0;
    color: var(--white);
    font-weight: 700;
    font-size: 44px;
    line-height: 52px;
    text-align: center;
    letter-spacing: 0.5px;
    text-transform: uppercase;
  }
  .radar {
    position: absolute;
    left: 0; top: 0;
    width: 1200px;
    height: 1200px;
  }
  .ring-label {
    font-family: "Montserrat", sans-serif;
    font-weight: 700;
    font-size: 22px;
    letter-spacing: 2.5px;
    fill: var(--white);
  }
  .item {
    font-family: "Lato", sans-serif;
    font-weight: 700;
    font-size: 11px;
  }
  .item-light { fill: var(--white); }
  .item-dark { fill: var(--navy); }
  .axis-box {
    position: absolute;
    background: var(--teal);
    border-radius: 13px;
    color: var(--white);
    display: flex;
    flex-direction: column;
    align-items: center;
    justify-content: center;
    text-align: center;
    font-weight: 700;
    text-transform: uppercase;
  }
  .axis-name {
    font-size: 20px;
    line-height: 24px;
  }
  .axis-note {
    font-size: 13px;
    line-height: 16px;
  }
  .axis-process { left: 496px; top: 296px; width: 208px; height: 65px; }
  .axis-task { left: 913px; top: 632px; width: 213px; height: 87px; }
  .axis-insights { left: 75px; top: 629px; width: 213px; height: 93px; }
  .axis-strategy { left: 483px; top: 991px; width: 233px; height: 72px; }
  .brand {
    position: absolute;
    right: 92px;
    top: 1108px;
    display: flex;
    align-items: center;
    gap: 10px;
    color: var(--navy);
    font-weight: 700;
  }
  .brand-mark {
    width: 18px;
    height: 18px;
    background: var(--teal);
  }
  .brand-name {
    font-size: 28px;
    line-height: 32px;
  }
</style>
</head>
<body>
<div class="canvas">
  <header class="header">
    <h1 class="title">Machine Learning Prospect Compass<br>for Tender Replies</h1>
  </header>

  <svg class="radar" viewBox="0 0 1200 1200" aria-label="Compass of four capability areas">
    <defs>
      <path id="arc-top-left" d="M348,675 A252,252 0 0 1 600,423"/>
      <path id="arc-top-right" d="M600,423 A252,252 0 0 1 852,675"/>
      <path id="arc-bottom-left" d="M332,675 A268,268 0 0 0 600,943"/>
      <path id="arc-bottom-right" d="M600,943 A268,268 0 0 0 868,675"/>
    </defs>

    <g stroke="var(--teal)" stroke-width="6">
      <line x1="600" y1="360" x2="600" y2="380"/>
      <line x1="600" y1="970" x2="600" y2="992"/>
      <line x1="286" y1="675" x2="305" y2="675"/>
      <line x1="895" y1="675" x2="914" y2="675"/>
    </g>

    <circle cx="600" cy="675" r="297" fill="var(--teal)"/>
    <circle cx="600" cy="675" r="292" fill="var(--navy)"/>
    <circle cx="600" cy="675" r="228" fill="var(--white)"/>

    <path d="M600,675 L382,675 A218,218 0 0 1 600,457 Z" fill="var(--teal)"/>
    <path d="M600,675 L600,457 A218,218 0 0 1 818,675 Z" fill="var(--ice)"/>
    <path d="M600,675 L818,675 A218,218 0 0 1 600,893 Z" fill="var(--teal)"/>
    <path d="M600,675 L600,893 A218,218 0 0 1 382,675 Z" fill="var(--ice)"/>

    <g stroke="var(--white)" stroke-width="3.5">
      <line x1="600" y1="384" x2="600" y2="966"/>
      <line x1="309" y1="675" x2="891" y2="675"/>
    </g>

    <text class="ring-label"><textPath href="#arc-top-left" startOffset="50%" text-anchor="middle">DECISION SUPPORT</textPath></text>
    <text class="ring-label"><textPath href="#arc-top-right" startOffset="50%" text-anchor="middle">PROPOSAL DEVELOPMENT</textPath></text>
    <text class="ring-label"><textPath href="#arc-bottom-left" startOffset="50%" text-anchor="middle">CAPTURE STRATEGY</textPath></text>
    <text class="ring-label"><textPath href="#arc-bottom-right" startOffset="50%" text-anchor="middle">PROPOSAL STRATEGY</textPath></text>

    <g class="item item-light" text-anchor="end">
      <text x="584" y="551">BID/NO BID ANALYSIS</text>
      <text x="584" y="571">BID QUALIFICATION</text>
      <text x="584" y="591">OPPORTUNITY ASSESSMENT</text>
      <text x="584" y="612">WIN PROBABILITY MODELING</text>
      <text x="584" y="632">STRATEGIC PRICING OPTIMIZATION</text>
      <text x="584" y="652">COMPLIANCE ASSESSMENT</text>
    </g>

    <g class="item item-dark">
      <text x="616" y="511">COMPANY PROFILE</text>
      <text x="616" y="529">CV AND RESUMES</text>
      <text x="616" y="546">PAST PERFORMANCE</text>
      <text x="616" y="564">TECHNICAL SOLUTION</text>
      <text x="616" y="581">COMPLIANCE MATRIX</text>
      <text x="616" y="599">STATEMENT OF WORK</text>
      <text x="616" y="616">EXECUTIVE SUMMARY</text>
      <text x="616" y="634">SECURITY QUESTIONNAIRES</text>
      <text x="616" y="651">DUE DILIGENCE QUESTIONNAIRES</text>
    </g>

    <g class="item item-dark" text-anchor="end">
      <text x="584" y="708">CAPTURE PLAN</text>
      <text x="584" y="730">SWOT ANALYSIS</text>
      <text x="584" y="753">CUSTOMER HOT BUTTONS</text>
      <text x="584" y="775">CUSTOMER INTELLIGENCE</text>
      <text x="584" y="798">COMPETITIVE INTELLIGENCE</text>
      <text x="584" y="820">VALUE PROPOSITION</text>
    </g>

    <g class="item item-light">
      <text x="616" y="708">PROPOSAL PLAN</text>
      <text x="616" y="730">PROPOSAL OUTLINE</text>
      <text x="616" y="752">DIFFERENTIATORS</text>
      <text x="616" y="774">WIN THEME</text>
      <text x="616" y="795">EXTRACTION</text>
      <text x="616" y="817">KEY MESSAGES</text>
      <text x="616" y="839">EXTRACTION</text>
    </g>
  </svg>

  <div class="axis-box axis-process">
    <span class="axis-name">Process<br>Enhancement</span>
  </div>
  <div class="axis-box axis-task">
    <span class="axis-name">Task<br>Automation</span>
    <span class="axis-note">(Foundational Use)</span>
  </div>
  <div class="axis-box axis-insights">
    <span class="axis-name">Insights<br>Generation</span>
    <span class="axis-note">(Transformative<br>Application)</span>
  </div>
  <div class="axis-box axis-strategy">
    <span class="axis-name">Strategy<br>Enablement</span>
  </div>

  <div class="brand">
    <span class="brand-mark"></span>
    <span class="brand-name">Quillon Partners</span>
  </div>
</div>
</body>
</html>
```